Menu Design marlowe

I need to create a take out menu for my restaurant something nice with some pictures. clean and simple with the colors of my reatsurant. which are orange and black. mostly black.

its fairly simple it has to be 4 pages front cover, inside front menu then 2nd page front and back with menu then 3rd page back front menu, back 3rd sushi menu with specials. final page 4th page, back map with adress and opening hours. and back cover final.

simple elegant and class. black and orange i will send logo and menu as well and pictures.

i am a high end bistro that serves gourmet pizza and pasta. we also have a sushi bar.
the menu will be 6 inches width by 9 inches

the menu that i sent is a pdf file. had an error with word please change font and make a new word dosument.

thank you

Industry/Entity Type

Restaurant

Requirements
Must have
• the colors which are black and orange. mostly black.

```html
<!DOCTYPE html>
<html lang="fr">
<head>
<meta charset="utf-8">
<title>marlowe — menu</title>
<link rel="stylesheet" href="https://fonts.googleapis.com/css2?family=Patrick+Hand&family=Patrick+Hand+SC&display=swap">
<style>
  :root {
    --backdrop: #ffffff;
    --orange: #e8821e;
    --orange-text: #f08a24;
    --panel: rgba(22, 22, 22, 0.82);
    --ink: #141414;
    --photo-dark: #2a2a2a;
    --photo-mid: #6d6d6d;
    --photo-light: #c9c9c9;
  }
  * { box-sizing: border-box; margin: 0; padding: 0; }
  html, body { width: 1200px; height: 1200px; overflow: hidden; background: var(--backdrop); }
  .canvas { position: relative; width: 1200px; height: 1200px; }
  .spread { position: absolute; left: 80px; top: 210px; width: 1040px; height: 780px; display: flex; box-shadow: 0 18px 40px rgba(0,0,0,0.18); }
  .page { position: relative; width: 520px; height: 780px; overflow: hidden; }

  .photo { position: absolute; inset: 0; }
  .photo--kitchen {
    background: linear-gradient(160deg, var(--photo-light) 0%, var(--photo-mid) 38%, var(--photo-dark) 72%, #4a4a4a 100%);
  }
  .photo--chefs {
    background: linear-gradient(180deg, #8a8a8a 0%, #5a5a5a 22%, #2e2e2e 45%, #1c1c1c 70%, #6e6e6e 100%);
  }

  .menu-panel { position: absolute; left: 35px; top: 0; width: 420px; height: 780px; background: var(--panel); font-family: "Patrick Hand SC", cursive; color: var(--orange-text); }
  .section { position: relative; z-index: 1; margin-bottom: 4px; }
  .section-title { height: 36px; background: var(--orange); color: var(--ink); font-size: 21px; font-weight: 400; text-align: center; line-height: 38px; letter-spacing: 1px; }
  .section-note { font-size: 12px; line-height: 14px; padding: 5px 18px 3px; }
  .items { list-style: none; padding: 0 22px 0 20px; }
  .item { display: flex; justify-content: space-between; align-items: flex-start; font-size: 12px; line-height: 14px; padding: 4px 0; }
  .item .price { white-space: nowrap; margin-left: 10px; }

  .faint-name { position: absolute; right: 24px; bottom: 2px; z-index: 0; font-family: "Patrick Hand", cursive; font-size: 38px; line-height: 40px; color: rgba(230,230,230,0.30); }
  .wall-name { position: absolute; right: 40px; top: 40px; font-family: "Patrick Hand", cursive; font-size: 72px; color: #2c2c2c; }

  .tip-note { position: absolute; left: 30px; top: 600px; width: 380px; background: var(--orange); color: var(--ink); font-family: "Patrick Hand", cursive; font-size: 17px; line-height: 21px; padding: 8px 12px 14px; }
  .tip-note p + p { margin-top: 4px; }
</style>
</head>
<body>
<div class="canvas">
  <div class="spread">
    <section class="page page--menu">
      <div class="photo photo--kitchen" role="img" aria-label="Black and white photo of the restaurant kitchen counter with trays and equipment"></div>
      <div class="menu-panel">
        <div class="section entrees">
          <h2 class="section-title">ENTREES / APPETIZERS</h2>
          <p class="section-note">SERVI AVEC 2 CHOIX DE SALADE VERTE, LEGUMES DU JOUR, RIZ OU FRITES<br>SERVED WITH A CHOICE OF GREEN SALADE, VEGETABLES, RICE OR FRIES</p>
          <ul class="items">
            <li class="item"><span>FISH N CHIPS</span><span class="price">$19.50</span></li>
            <li class="item"><span>SAUMON GRILLE / GRILLED SALMON</span><span class="price">$21.95</span></li>
            <li class="item"><span>TILAPIA AU FOUR</span><span class="price">$19.50</span></li>
            <li class="item"><span>OVEN ROASTED TILAPIA<br>STEAK DE THON STYLE TATAKI / TATAKI STYLE TUNA STEAK</span><span class="price">$25.95</span></li>
            <li class="item"><span>CREVETTES SAUTEES A L'AIL (10)</span><span class="price">$21.95</span></li>
          </ul>
        </div>
        <div class="section sides">
          <h2 class="section-title">A COTES / SIDES</h2>
          <ul class="items">
            <li class="item"><span>FRITES / FRENCH FRIES</span><span class="price">$3.50</span></li>
            <li class="item"><span>FRITES EPICEES / SPICY FRENCH FRIES</span><span class="price">$4.50</span></li>
            <li class="item"><span>SWEET POTATOES FRIES / FRITE POMME DE TERRE DOUCE</span><span class="price">$4.95</span></li>
            <li class="item"><span>RIZ / RICE</span><span class="price">$3.00</span></li>
            <li class="item"><span>LEGUMES GRILLES DE SAISON / SEASONAL GRILLED VEGETABLES</span><span class="price">$5.95</span></li>
            <li class="item"><span>PATATES / POTATOES</span><span class="price">$3.50</span></li>
            <li class="item"><span>SALADE VERTE / GREEN SALAD</span><span class="price">$3.25</span></li>
            <li class="item"><span>THON / TUNA</span><span class="price">$3.00</span></li>
            <li class="item"><span>OEUF DUR / BOILED EGG</span><span class="price">$2.00</span></li>
          </ul>
        </div>
        <div class="section pasta">
          <h2 class="section-title">PATES / PASTA</h2>
          <p class="section-note">SAUCES: TOMATE - ARABIATA - ALFREDO - PESTO &amp; AIL - BELLA ROSA - MARSALA CHAMPIGNON</p>
          <ul class="items">
            <li class="item"><span>SPAGHETTI</span><span class="price">$14.95</span></li>
            <li class="item"><span>PENNE</span><span class="price">$14.95</span></li>
            <li class="item"><span>FETTUCCINI</span><span class="price">$14.95</span></li>
            <li class="item"><span>RAVIOLI AUX CHAMPIGNONS SAUVAGES<br>WILD MUSHROOM RAVIOLI</span><span class="price">$17.50</span></li>
            <li class="item"><span>RAVIOLI A LA RICOTTA EPINARDS<br>RAVIOLI WITH RICOTTA &amp; SPINACH</span><span class="price">$17.50</span></li>
            <li class="item"><span>RAVIOLI A LA POMME DE TERRE DOUCE<br>SWEET POTATOES RAVIOLI</span><span class="price">$17.50</span></li>
            <li class="item"><span>LASAGNE VEGETARIENNE<br>VEGGIE LASAGNA<br>SUR DEMANDE</span><span class="price">$14.95</span></li>
          </ul>
        </div>
        <span class="faint-name">marlowe</span>
      </div>
    </section>

    <section class="page page--kitchen">
      <div class="photo photo--chefs" role="img" aria-label="Black and white photo of two chefs in caps and black jackets preparing food in the kitchen"></div>
      <span class="wall-name">marlowe</span>
      <div class="tip-note">
        <p>Un pourboire de 15 % sera ajouté automatiquement sur la facture</p>
        <p>A tip of 15 % will be added automatically on the bill</p>
      </div>
    </section>
  </div>
</div>
</body>
</html>
```